Sleek wordpress site for Brightwell finishing systems

We are a commercial job shop that serves B2B, govt & LEO and retail clients.We need a wordpress site with 6 individual pages: homepage, coating, laser engraving, laser cutting, part marking, and contact us. I have attached an outline of the desired flow and sub headings for each page. I would like to incorporate the colors of the logo through out the site to be clean and sleek enough to appeal to B2B commercial clients yet be inviting enough for retail clients.

I would like to have easy picture functionality so photographs on each page can be updated easily.

Target Market(s)

B2B industrial & Govt and Military part marking, laser engraving and coating: machine shops, aerospace companies, tool manufactures. Retail: personalized gifts, Job Shop

Coding

Coded - Design and coding required

Font styles to use
Sans Serif
Other font styles liked:
• Open to suggestion

Colors
0255a3
3176b5
eaf1f7
cfdeed
ffffff

Requirements
Must have
• Clean easy to navigate flow, separate pages as indicated on attached outline, high class feel. Great picture functionality, professional and inviting feel,
• **update: needs to be optimized for mobile, should have a gallery function. Gallery can be an additional page or embedded
Nice to have
• Social media connectivity links,
Should not have
• crappy plugins that make back-end management difficult, no blog

```html
<!DOCTYPE html>
<html lang="en">
<head>
<meta charset="utf-8">
<title>Brightwell Finishing Systems</title>
<link href="https://fonts.googleapis.com/css2?family=Lato:wght@400;700;900&display=swap" rel="stylesheet">
<style>
:root{
  --brand:#0255a3;
  --brand-deep:#0a4294;
  --brand-mid:#3176b5;
  --field:#e4ebf5;
  --contact-bg:#c5d6e9;
  --soft:#f4f4f4;
  --ink:#1b1b1b;
  --white:#ffffff;
}
*{margin:0;padding:0;box-sizing:border-box}
html,body{width:1200px;height:2278px;overflow:hidden}
body{font-family:'Lato',sans-serif;color:var(--ink);background:var(--white);position:relative}
.abs{position:absolute}
.site-header{position:absolute;left:0;top:0;width:1200px;height:121px;background:var(--white)}
.brand{left:76px;top:34px;display:flex;align-items:center;gap:12px;color:var(--brand)}
.brand-dot{width:44px;height:44px;border-radius:50%;background:var(--brand)}
.brand-name{font-weight:900;font-size:19px;line-height:1.15;text-transform:uppercase;width:180px}
.call-btn{left:769px;top:47px;width:206px;height:35px;background:var(--brand);color:var(--white);font-weight:700;font-size:15px;display:flex;align-items:center;justify-content:center;letter-spacing:.3px}
.social-top{left:993px;top:55px;display:flex;gap:22px;align-items:center}
.social-top span{width:16px;height:16px;border-radius:50%;background:#222}
.main-nav{position:absolute;left:0;top:121px;width:1200px;height:52px;background:var(--brand)}
.main-nav a{position:absolute;top:18px;color:var(--white);font-size:14px;font-weight:700;text-decoration:none;letter-spacing:.2px}
.hero{position:absolute;left:0;top:173px;width:1200px;height:467px;background:linear-gradient(100deg,#dfe4ea 0%,#c9d2de 12%,#6f8fc7 30%,#5e82c4 55%,#e6e9ee 72%,#8aa2cc 100%)}
.hero svg{position:absolute;top:200px}
.section-title{position:absolute;left:0;width:1200px;text-align:center;font-weight:900;font-size:32px;letter-spacing:.5px;color:var(--ink)}
.divider{position:absolute;left:517px;width:166px;height:2px;background:#c8c8c8}
.divider::after{content:"";position:absolute;left:50px;top:-1px;width:66px;height:4px;background:#a9a9a9;border-radius:2px}
.services{position:absolute;left:0;top:640px;width:1200px;height:400px;background:var(--soft)}
.service{position:absolute;top:124px;width:247px}
.service-photo{width:247px;height:173px}
.service-name{margin-top:17px;text-align:center;font-size:17px;font-weight:700;text-transform:uppercase}
.about{position:absolute;left:0;top:1040px;width:1200px;height:342px;background:var(--white)}
.about p{position:absolute;left:262px;top:116px;width:676px;text-align:center;font-size:14.6px;line-height:24px}
.pill{position:absolute;left:532px;width:136px;height:37px;border-radius:19px;background:var(--brand);color:var(--white);font-size:15px;display:flex;align-items:center;justify-content:center;text-transform:uppercase}
.contact{position:absolute;left:0;top:1382px;width:1200px;height:549px;background:var(--contact-bg)}
.field{position:absolute;background:var(--field);font-size:13px;font-weight:700;padding:13px 18px;text-transform:uppercase}
.site-footer{position:absolute;left:0;top:1931px;width:1200px;height:347px;background:var(--brand-deep);color:var(--white)}
.col{position:absolute;top:64px}
.col h4{font-size:15.5px;font-weight:700;text-transform:uppercase;margin-bottom:20px}
.col li{list-style:none;font-size:14px;height:27.6px;display:flex;align-items:center;gap:17px}
.col li svg{flex:none}
.links li{font-weight:700;font-size:13px;text-transform:uppercase}
.circles{display:flex;gap:11px}
.circles span{width:33px;height:33px;border:2px solid var(--white);border-radius:50%}
.info li{gap:12px;align-items:flex-start;height:auto;line-height:28px}
.bottom-bar{position:absolute;left:0;top:294px;width:1200px;height:53px;border-top:1px solid #2a5aa4;text-align:center;font-size:13px;font-weight:700;line-height:53px}
</style>
</head>
<body>
<header class="site-header">
  <div class="abs brand"><span class="brand-dot"></span><span class="brand-name">Brightwell Finishing Systems</span></div>
  <div class="abs call-btn">CALL US : 480.555.0142</div>
  <div class="abs social-top">
    <span></span><span></span><span></span>
    <svg width="17" height="14" viewBox="0 0 17 14"><rect x="1" y="1" width="15" height="12" rx="2" fill="none" stroke="#222" stroke-width="1.8"/><path d="M1.5 2 8.5 8 15.5 2" fill="none" stroke="#222" stroke-width="1.8"/></svg>
  </div>
</header>
<nav class="main-nav">
  <a style="left:76px">HOME</a><a style="left:149px">COATING</a><a style="left:243px">LASER ENGRAVING</a><a style="left:398px">LASER CUTTING</a><a style="left:532px">PART MARKING</a><a style="left:665px">CONTACT US.</a>
</nav>
<section class="hero" role="img" aria-label="Technician in protective suit spraying a coating with a spray gun">
  <svg style="left:118px" width="20" height="30" viewBox="0 0 20 30"><path d="M16 3 4 15 16 27" fill="none" stroke="#fff" stroke-width="4"/></svg>
  <svg style="left:1070px" width="20" height="30" viewBox="0 0 20 30"><path d="M4 3 16 15 4 27" fill="none" stroke="#fff" stroke-width="4"/></svg>
</section>
<section class="services">
  <h2 class="section-title" style="top:24px">OUR SERVICES</h2>
  <div class="divider" style="top:85px"></div>
  <div class="service" style="left:74px"><div class="service-photo" role="img" aria-label="Laser engraving machine at work" style="background:linear-gradient(135deg,#8d9aa8,#3e4a58 60%,#a9b4c0)"></div><div class="service-name">Laser Engraving</div></div>
  <div class="service" style="left:342px"><div class="service-photo" role="img" aria-label="Laser cutting a metal sheet" style="background:linear-gradient(135deg,#2a2a2a,#9a9a9a 55%,#3a3a3a)"></div><div class="service-name">Laser Cutting</div></div>
  <div class="service" style="left:611px"><div class="service-photo" role="img" aria-label="Hands marking a metal part" style="background:linear-gradient(135deg,#7a4a36,#c98a6a 50%,#5e3a2c)"></div><div class="service-name">Part Marking</div></div>
  <div class="service" style="left:878px"><div class="service-photo" role="img" aria-label="Spray coating hanging metal parts" style="background:linear-gradient(135deg,#1e1e1e,#6c6c6c 55%,#2a2a2a)"></div><div class="service-name">Coatings</div></div>
</section>
<section class="about">
  <h2 class="section-title" style="top:46px">WHAT IS CERALUX</h2>
  <div class="divider" style="top:98px"></div>
  <p>Ceralux is a spray on ceramic based finish that can be applied to metals, plastics, polymers and wood. The unique formulation used for Ceralux ceramic coating enhances a number of physical performance properties including abrasion/wear resistance, corrosion resistance, chemical resistance, impact strength, and hardness. Ceralux ceramic coatings utilize state-of-the-art technology to out-perform any competitive coating in both laboratory settings and real world applications, making it ideal for firearm finishes.</p>
  <div class="pill" style="top:250px">Read More</div>
</section>
<section class="contact">
  <h2 class="section-title" style="top:56px">CONTACT US</h2>
  <div class="field" style="left:251px;top:154px;width:341px;height:36px">First Name</div>
  <div class="field" style="left:606px;top:154px;width:342px;height:36px">Last Name</div>
  <div class="field" style="left:251px;top:210px;width:341px;height:36px">Email</div>
  <div class="field" style="left:606px;top:210px;width:342px;height:36px">Phone</div>
  <div class="field" style="left:251px;top:266px;width:697px;height:152px">Message</div>
  <div class="pill" style="top:442px">Submit</div>
</section>
<footer class="site-footer">
  <div class="col links" style="left:76px;top:62px"><h4>Quick Links</h4><ul>
    <li><svg width="7" height="10"><path d="M1 1 5 5 1 9" fill="none" stroke="#fff" stroke-width="2"/></svg>Home</li>
    <li><svg width="7" height="10"><path d="M1 1 5 5 1 9" fill="none" stroke="#fff" stroke-width="2"/></svg>Coating</li>
    <li><svg width="7" height="10"><path d="M1 1 5 5 1 9" fill="none" stroke="#fff" stroke-width="2"/></svg>Laser Engraving</li>
    <li><svg width="7" height="10"><path d="M1 1 5 5 1 9" fill="none" stroke="#fff" stroke-width="2"/></svg>Laser Cutting</li>
    <li><svg width="7" height="10"><path d="M1 1 5 5 1 9" fill="none" stroke="#fff" stroke-width="2"/></svg>Part Marking</li>
    <li><svg width="7" height="10"><path d="M1 1 5 5 1 9" fill="none" stroke="#fff" stroke-width="2"/></svg>Contact Us.</li>
  </ul></div>
  <div class="col" style="left:368px"><h4>Services</h4><ul>
    <li><svg width="7" height="10"><path d="M1 1 5 5 1 9" fill="none" stroke="#fff" stroke-width="2"/></svg>Laser engraving</li>
    <li><svg width="7" height="10"><path d="M1 1 5 5 1 9" fill="none" stroke="#fff" stroke-width="2"/></svg>Laser Cutting</li>
    <li><svg width="7" height="10"><path d="M1 1 5 5 1 9" fill="none" stroke="#fff" stroke-width="2"/></svg>Part Marking</li>
    <li><svg width="7" height="10"><path d="M1 1 5 5 1 9" fill="none" stroke="#fff" stroke-width="2"/></svg>Coatings</li>
  </ul></div>
  <div class="col" style="left:623px;top:70px"><h4>Follow Us</h4><div class="circles"><span></span><span></span><span></span><span></span></div></div>
  <div class="col info" style="left:924px"><h4>Contact Us</h4><ul>
    <li><svg width="13" height="28" viewBox="0 0 13 28"><path d="M3 8c1-1 2-1 3 1l1 2c0 1-1 1-1 2 1 2 2 3 4 4 1 0 1-1 2-1l1 1c1 1 1 2 0 3-2 2-5 1-8-2S1 10 3 8z" fill="#fff"/></svg>480.555.0142</li>
    <li><svg width="13" height="28" viewBox="0 0 13 28"><rect x="0" y="10" width="13" height="9" rx="1" fill="#fff"/><path d="M0 11 6.5 15 13 11" fill="none" stroke="#0a4294" stroke-width="1.2"/></svg>info@brightwellfinish.com</li>
    <li><svg width="13" height="28" viewBox="0 0 13 28"><path d="M6.5 8a4.5 4.5 0 0 1 4.5 4.5c0 3-4.5 7.5-4.5 7.5S2 15.5 2 12.5A4.5 4.5 0 0 1 6.5 8z" fill="#fff"/><circle cx="6.5" cy="12.5" r="1.6" fill="#0a4294"/></svg>418 W Alder Ave #210,<br>Mesa, AZ 85201</li>
  </ul></div>
  <div class="bottom-bar">© 2018 | &nbsp;www.brightwellfinish.com &nbsp;. &nbsp;Privacy Policy &nbsp;. &nbsp;Terms of use</div>
</footer>
</body>
</html>
```